R&K Security Services PTY. LTD.

Ive just had my logo made and I'm looking for some simple but strong designs for my business cards the company is a security company.

Please use dark colors.

Regards,

Dale Prentiss

Reason: Need more time for discussion with other directors

Industry/Entity Type

Security

Font styles to use
Sans Serif
Decorative

```html
<!DOCTYPE html>
<html lang="en">
<head>
<meta charset="utf-8">
<title>R&amp;K Security Services – Business Card</title>
<link rel="stylesheet" href="https://fonts.googleapis.com/css2?family=Open+Sans:wght@400;600;700&display=swap">
<style>
  :root {
    --page-bg: #e6e6ea;
    --card-white: #ffffff;
    --card-grey: #8c8c8c;
    --band-grey: #9a9a9a;
    --ink-dark: #1e1e1e;
    --ink-mid: #7a7a7a;
    --stripe-dark: #232323;
    --divider: #b5b5b5;
    --on-grey: #ffffff;
  }
  * { box-sizing: border-box; margin: 0; padding: 0; }
  html, body {
    width: 1200px; height: 987px; overflow: hidden;
    background: var(--page-bg);
    font-family: "Open Sans", sans-serif;
  }
  .stage {
    width: 1200px; height: 987px;
    display: flex; align-items: center; justify-content: center; gap: 40px;
  }
  .card {
    position: relative;
    width: 540px; height: 310px;
    border-radius: 20px;
    overflow: hidden;
    box-shadow: 0 6px 18px rgba(0,0,0,0.15);
  }
  .card--front { background: var(--card-white); }
  .card--back { background: var(--card-grey); }

  .card__shapes { position: absolute; inset: 0; }

  .brand {
    position: absolute;
    display: flex; align-items: center; gap: 10px;
    color: var(--ink-dark);
    font-weight: 700;
    line-height: 1.15;
  }
  .brand__mark { width: 18px; height: 18px; background: currentColor; flex: none; }
  .card--front .brand { left: 34px; top: 70px; width: 210px; font-size: 21px; }
  .card--back .brand {
    left: 50%; top: 92px; transform: translateX(-50%);
    color: var(--on-grey); font-size: 28px; width: 360px; justify-content: center;
  }

  .divider {
    position: absolute; left: 262px; top: 36px;
    width: 1px; height: 148px; background: var(--divider);
  }

  .contact { position: absolute; left: 282px; top: 30px; color: var(--ink-dark); }
  .contact__name { font-weight: 700; font-size: 19px; line-height: 1.2; }
  .contact__role { font-size: 15px; color: var(--ink-mid); line-height: 1.3; margin-bottom: 8px; }
  .contact__row {
    display: flex; align-items: center; gap: 6px;
    font-size: 14px; line-height: 1.45;
  }
  .contact__row svg { width: 12px; height: 12px; fill: var(--ink-mid); flex: none; }
  .contact__address { font-size: 14px; line-height: 1.35; margin-top: 6px; }

  .website {
    position: absolute;
    color: var(--on-grey);
    letter-spacing: 4px;
    font-size: 16px;
    white-space: nowrap;
  }
  .card--front .website { left: 40px; bottom: 20px; }
  .card--back .website { left: 0; right: 0; top: 200px; text-align: center; font-size: 18px; }
</style>
</head>
<body>
<main class="stage">

  <section class="card card--front" aria-label="Business card front">
    <svg class="card__shapes" viewBox="0 0 540 310" aria-hidden="true">
      <polygon points="0,196 232,196 250,212 0,212" fill="var(--stripe-dark)"/>
      <polygon points="0,220 254,220 278,244 540,244 540,310 0,310" fill="var(--band-grey)"/>
    </svg>

    <div class="brand"><span class="brand__mark"></span><span>R&amp;K Security Services</span></div>

    <div class="divider"></div>

    <div class="contact">
      <p class="contact__name">Dale Prentiss</p>
      <p class="contact__role">Director</p>
      <p class="contact__row">
        <svg viewBox="0 0 24 24"><path d="M6.6 10.8a15 15 0 0 0 6.6 6.6l2.2-2.2a1 1 0 0 1 1-.25 11.4 11.4 0 0 0 3.6.57 1 1 0 0 1 1 1V20a1 1 0 0 1-1 1A17 17 0 0 1 3 4a1 1 0 0 1 1-1h3.5a1 1 0 0 1 1 1c0 1.250.2 2.45.57 3.6a1 1 0 0 1-.25 1z"/></svg>
        012-345-6789
      </p>
      <p class="contact__row">
        <svg viewBox="0 0 24 24"><path d="M7 1h10a2 2 0 0 1 2 2v18a2 2 0 0 1-2 2H7a2 2 0 0 1-2-2V3a2 2 0 0 1 2-2zm0 3v14h10V4zm5 15.5a1.2 1.2 0 1 0 0 2.4 1.2 1.2 0 0 0 0-2.4z"/></svg>
        012-345-6789
      </p>
      <p class="contact__row">
        <svg viewBox="0 0 24 24"><path d="M2 5h20v14H2zm2 2v.5l8 5 8-5V7zm0 2.8V17h16V9.8l-8 5z"/></svg>
        info@rkguardsecure.com
      </p>
      <p class="contact__address">Citi Name, Street Name<br>Zip Code-00000</p>
    </div>

    <p class="website">www.rkguardsecure.com</p>
  </section>

  <section class="card card--back" aria-label="Business card back">
    <div class="brand"><span class="brand__mark"></span><span>R&amp;K Security Services</span></div>
    <p class="website">www.rkguardsecure.com</p>
  </section>

</main>
</body>
</html>
```